Business Card Design Project - Zorvex Labs

High quality business card Must be funky.

We are an IT support from home and office, but our image is more retro.

Our logo is black and lime green. IT should be a 2 sided card with the multiple coloured ties somehow used on the reverse side (be creative!)

Black or white background fine or a combo of both

Target Market(s)

consumer and business

Industry/Entity Type

Business

```html
<!DOCTYPE html>
<html lang="en">
<head>
<meta charset="utf-8">
<title>Zorvex Labs — Business Card</title>
<link href="https://fonts.googleapis.com/css2?family=Oswald:wght@300;400&display=swap" rel="stylesheet">
<style>
  :root {
    --ink-black: #221e1c;
    --tagline-grey: #3b3633;
    --paper: #ffffff;
    --edge-grey: #c9c9c9;
    --stripe-yellow: #dde86a;
    --stripe-blue: #8ecff4;
    --stripe-red: #e8334a;
    --stripe-green: #a6e33a;
    --lime: #b5e53d;
    --cyan: #2ab0d8;
    --title-blue: #2a9bd1;
    --rule-green: #3aa56e;
    --dot-red: #d4161f;
    --dot-pink: #e84a78;
    --text-dark: #231f20;
  }
  * { margin: 0; padding: 0; box-sizing: border-box; }
  html, body { width: 955px; height: 1200px; overflow: hidden; background: var(--paper); }
  body { position: relative; font-family: "Oswald", sans-serif; color: var(--text-dark); }

  .card { position: absolute; left: 0; width: 955px; border: 1px solid var(--edge-grey); overflow: hidden; background: var(--paper); }
  .card--front { top: 0; height: 546px; }
  .card--back { top: 655px; height: 545px; }

  .front-panel { position: absolute; left: 0; top: 0; width: 100%; height: 494px; background: var(--ink-black); }

  .stripes { position: absolute; left: 0; width: 100%; }
  .stripes span { display: block; width: 100%; }
  .stripes .s-yellow { background: var(--stripe-yellow); height: 14px; }
  .stripes .s-blue { background: var(--stripe-blue); height: 13px; }
  .stripes .s-red { background: var(--stripe-red); height: 11px; }
  .stripes .s-green { background: var(--stripe-green); height: 11px; }
  .card--front .stripes { top: 494px; }
  .card--back .stripes { top: 495px; }

  .brand-name { position: absolute; font-family: "Oswald", sans-serif; font-weight: 400; white-space: nowrap; line-height: 1; }
  .brand-name--front { left: 0; width: 100%; top: 168px; text-align: center; font-size: 104px; color: var(--lime); }
  .brand-name--back { left: 618px; top: 100px; font-size: 56px; color: var(--cyan); }

  .tagline { position: absolute; left: 0; width: 100%; top: 372px; text-align: center; font-size: 30px; letter-spacing: 1px; color: var(--tagline-grey); text-transform: uppercase; }

  .person { position: absolute; left: 23px; top: 178px; display: flex; align-items: baseline; }
  .person__name { font-size: 78px; font-weight: 400; line-height: 1; letter-spacing: -1px; color: var(--text-dark); text-transform: uppercase; }
  .person__role { margin-left: 12px; font-size: 20px; color: var(--title-blue); }
  .person-rule { position: absolute; left: 14px; top: 252px; width: 650px; height: 2px; background: var(--rule-green); }

  .contacts { position: absolute; left: 44px; top: 272px; list-style: none; }
  .contacts li { display: flex; align-items: center; height: 54px; font-size: 22px; font-weight: 300; }
  .contacts .marker { width: 10px; height: 22px; margin-right: 16px; border-radius: 2px; }
  .marker--red { background: var(--dot-red); }
  .marker--pink { background: var(--dot-pink); }
  .marker--lime { background: var(--lime); }
  .marker--cyan { background: var(--cyan); }
</style>
</head>
<body>
  <section class="card card--front" aria-label="Front of card">
    <div class="front-panel">
      <div class="brand-name brand-name--front">Zorvex Labs</div>
      <p class="tagline">Bringing an IT helpdesk to your front door</p>
    </div>
    <div class="stripes" aria-hidden="true">
      <span class="s-yellow"></span><span class="s-blue"></span><span class="s-red"></span><span class="s-green"></span>
    </div>
  </section>

  <section class="card card--back" aria-label="Back of card">
    <div class="brand-name brand-name--back">Zorvex Labs</div>
    <div class="person">
      <h1 class="person__name">Marisol</h1>
      <span class="person__role">Director</span>
    </div>
    <div class="person-rule"></div>
    <ul class="contacts">
      <li><span class="marker marker--red"></span>Email: marisol@zorvexlabs.asia</li>
      <li><span class="marker marker--pink"></span>Hotline: +256-700-418-252</li>
      <li><span class="marker marker--lime"></span>Mobile: +256-700-418-252</li>
      <li><span class="marker marker--cyan"></span>Web.: http://zorvexlabs.asia</li>
    </ul>
    <div class="stripes" aria-hidden="true">
      <span class="s-yellow"></span><span class="s-blue"></span><span class="s-red"></span><span class="s-green"></span>
    </div>
  </section>
</body>
</html>
```